Marisol business card and stationary
business card and stationary
Marisol business card and stationary - Retailers
Creative Brief
Bright & Fun-filled
Janet Wroblenko
owner, designer
marisol a florist 418 north brook lane greenville, sc 29174
info@marisolblooms.example
marisolblooms.example
Concepts
Stationery for Online Retailer

```html
<!DOCTYPE html>
<html lang="en">
<head>
<meta charset="utf-8">
<title>Marisol stationery set</title>
<link href="https://fonts.googleapis.com/css2?family=Nunito:wght@400;700&display=swap" rel="stylesheet">
<style>
:root{
  --bg:#ece8e3;
  --paper:#ffffff;
  --petal-light:#f4f4f4;
  --petal-mid:#e3e3e3;
  --brand:#e56f7c;
  --leaf:#8cb54c;
  --ink:#6a6a6a;
  --shadow:rgba(0,0,0,.18);
}
*{box-sizing:border-box;margin:0;padding:0}
html,body{width:1200px;height:998px;overflow:hidden}
body{background:var(--bg);font-family:"Nunito",sans-serif;color:var(--ink);position:relative}
.piece{position:absolute;background:var(--paper);box-shadow:0 3px 10px var(--shadow);overflow:hidden}
.petal-art{position:absolute;background:radial-gradient(circle at 45% 45%,var(--petal-light) 0%,var(--petal-mid) 45%,rgba(255,255,255,0) 72%);opacity:.9}
.brand{position:absolute;display:flex;align-items:center;gap:6px}
.brand-dot{border-radius:50%;background:var(--brand);flex:none}
.brand-name{font-weight:700;color:var(--brand);line-height:1}
.contact{position:absolute;font-size:8px;line-height:1.45;color:var(--ink)}
.contact strong{font-weight:700;color:var(--brand)}
/* business cards */
.card-front{left:68px;top:76px;width:243px;height:113px}
.card-back{left:338px;top:76px;width:250px;height:113px}
/* letterhead */
.letterhead{left:54px;top:238px;width:500px;height:707px}
/* envelopes */
.env-flap{left:608px;top:32px;width:560px;height:346px}
.flap-line{position:absolute;inset:0}
.env-dl{left:615px;top:405px;width:552px;height:265px}
.env-front{left:615px;top:689px;width:552px;height:270px}
</style>
</head>
<body>

<section class="piece card-front" aria-label="Business card front">
  <div class="petal-art" role="img" aria-label="Faint white dahlia petals" style="right:-40px;top:-30px;width:200px;height:180px"></div>
  <div class="brand" style="left:22px;top:40px">
    <span class="brand-dot" style="width:24px;height:24px"></span>
    <span class="brand-name" style="font-size:24px">marisol</span>
  </div>
</section>

<section class="piece card-back" aria-label="Business card back">
  <div class="petal-art" role="img" aria-label="Faint white dahlia petals" style="right:-50px;top:-20px;width:210px;height:170px"></div>
  <div class="brand" style="left:16px;top:40px">
    <span class="brand-dot" style="width:20px;height:20px"></span>
    <span class="brand-name" style="font-size:20px">marisol</span>
  </div>
  <div class="contact" style="left:150px;top:10px;font-size:6.5px">
    <strong>Janet Wroblenko</strong><br>owner, designer<br><br>
    marisol a florist<br>418 north brook lane<br>greenville, sc 29174<br><br>
    (864) 555-0142<br>info@marisolblooms.example<br>marisolblooms.example
  </div>
</section>

<section class="piece letterhead" aria-label="Letterhead">
  <div class="petal-art" role="img" aria-label="Faint white dahlia petals" style="right:-60px;top:30px;width:340px;height:320px"></div>
  <div class="brand" style="left:22px;top:40px">
    <span class="brand-dot" style="width:44px;height:44px"></span>
    <span class="brand-name" style="font-size:32px">marisol</span>
  </div>
  <div class="contact" style="right:26px;top:26px;text-align:right">
    Marisol A Florist<br>418 North Brook Lane<br>Greenville, SC 29174<br><br>
    (864) 555-0142<br>info@marisolblooms.example<br>marisolblooms.example
  </div>
</section>

<section class="piece env-flap" aria-label="Envelope back with flap">
  <svg class="flap-line" viewBox="0 0 560 346" aria-hidden="true"><polyline points="0,0 280,200 560,0" fill="none" stroke="#dcdcdc" stroke-width="1.5"/></svg>
  <div class="petal-art" role="img" aria-label="Faint white dahlia petals" style="right:-60px;top:10px;width:420px;height:380px"></div>
  <div class="brand" style="left:240px;top:20px">
    <span class="brand-dot" style="width:30px;height:30px"></span>
    <span class="brand-name" style="font-size:22px">marisol</span>
  </div>
  <div class="brand" style="left:16px;top:150px">
    <span class="brand-dot" style="width:40px;height:40px"></span>
    <span class="brand-name" style="font-size:30px">marisol</span>
  </div>
  <div class="contact" style="left:100px;top:196px">
    Marisol A Florist<br>418 North Brook Lane<br>Greenville, SC 29174
  </div>
</section>

<section class="piece env-dl" aria-label="Envelope back">
  <svg class="flap-line" viewBox="0 0 552 265" aria-hidden="true"><polyline points="0,0 276,90 552,0" fill="none" stroke="#dcdcdc" stroke-width="1.5"/></svg>
  <div class="petal-art" role="img" aria-label="Faint white dahlia petals" style="right:-40px;top:-40px;width:300px;height:200px"></div>
  <div class="brand" style="left:246px;top:16px">
    <span class="brand-dot" style="width:22px;height:22px"></span>
    <span class="brand-name" style="font-size:16px">marisol</span>
  </div>
</section>

<section class="piece env-front" aria-label="Envelope front">
  <div class="petal-art" role="img" aria-label="Faint white dahlia petals" style="right:-40px;top:-20px;width:380px;height:300px"></div>
  <div class="brand" style="left:16px;top:22px">
    <span class="brand-dot" style="width:40px;height:40px"></span>
    <span class="brand-name" style="font-size:30px">marisol</span>
  </div>
  <div class="contact" style="left:100px;top:96px">
    Marisol A Florist<br>418 North Brook Lane<br>Greenville, SC 29174
  </div>
</section>

</body>
</html>
```